Zanquorra Business Card Design

Zanquorra is a small and new restaurant/ bar location in Hong Kong. The name "Djibouti" derives from an African country. There is no specific reason behind other than the fact, that the bar is somewhat inspired by African elements (only inspired but not purely based on African cuisine etc.).

The bar is somewhat a fusion of African, Mediterranean and Oriental (Old French Vietnam) elements.

However, it is very imperative to stress, that the overall look and feel of Zanquorra is a very high end cocktail lounge/ bar location. The bar is tucked away in a hidden alley, so people will have to know about it. The idea is to send the consumer off in an Escape or hidden remote location where they are at ease in a hip, stylish and trendy environment.

The card needs to feel high-end.

Final logo artwork has been attached and also pictures of the bar/ restaurant itself. The logo ie monkey head cannot be modified. However, the background color and the color of the type "ZANQUORRA" can be changed.

The following details need to fit onto the business card. Of course they can be arranged to your liking:

LOGO

Colin Vey
Partner

+852 97035164
xxx@zanquorra.com
www.zanquorra.com
7C, Brennick Road, Wan Chai, Hong Kong

```html
<!DOCTYPE html>
<html lang="en">
<head>
<meta charset="utf-8">
<title>Zanquorra Business Card</title>
<link href="https://fonts.googleapis.com/css2?family=Cinzel:wght@700&family=Open+Sans:wght@400;600&display=swap" rel="stylesheet">
<style>
  :root {
    --backdrop: #d9d9d9;
    --card-white: #ffffff;
    --ink: #1e1a17;
    --accent-red: #d3202a;
    --accent-blue: #3b5bb5;
    --rule-blue: #4a6cc4;
    --back-red-light: #c8161e;
    --back-red-dark: #4a0407;
  }
  * { margin: 0; padding: 0; box-sizing: border-box; }
  html, body {
    width: 900px;
    height: 1200px;
    overflow: hidden;
    background: var(--backdrop);
  }
  .canvas {
    position: relative;
    width: 900px;
    height: 1200px;
  }
  .card {
    position: absolute;
    box-shadow: 0 6px 18px rgba(0,0,0,0.25);
  }
  .card-front {
    left: 280px;
    top: 60px;
    width: 340px;
    height: 595px;
    background: var(--card-white);
    display: flex;
    flex-direction: column;
    align-items: center;
    padding-top: 70px;
    font-family: "Open Sans", sans-serif;
    color: var(--ink);
    text-align: center;
  }
  .brand-mark {
    width: 120px;
    height: 120px;
    border-radius: 50%;
    background: var(--ink);
  }
  .brand-name {
    margin-top: 22px;
    font-family: "Cinzel", serif;
    font-weight: 700;
    font-size: 34px;
    letter-spacing: 1px;
    color: var(--ink);
  }
  .person-name {
    margin-top: 26px;
    font-size: 20px;
    font-weight: 600;
    letter-spacing: 1px;
    color: var(--accent-red);
  }
  .person-role {
    margin-top: 2px;
    font-size: 10px;
    letter-spacing: 2px;
    color: var(--accent-blue);
  }
  .contact {
    margin-top: 22px;
    font-size: 14px;
    line-height: 1.55;
  }
  .rule {
    width: 70px;
    height: 2px;
    margin: 14px auto;
    background: var(--rule-blue);
  }
  .card-back {
    left: 152px;
    top: 745px;
    width: 595px;
    height: 340px;
    background: linear-gradient(135deg, var(--back-red-dark) 0%, #7a0a10 40%, var(--back-red-light) 100%);
  }
</style>
</head>
<body>
<main class="canvas">
  <section class="card card-front">
    <div class="brand-mark"></div>
    <div class="brand-name">ZANQUORRA</div>
    <div class="person-name">COLIN VEY</div>
    <div class="person-role">PARTNER</div>
    <div class="contact">
      <p>P : +852 97035164</p>
      <p>M: 604.318.2275</p>
      <div class="rule"></div>
      <p>7C, Brennick Road, Wan Chai,</p>
      <p>Hong Kong</p>
      <div class="rule"></div>
      <p>xxx@zanquorra.com</p>
      <p>www.zanquorra.com</p>
    </div>
  </section>
  <section class="card card-back" role="img" aria-label="Repeating pattern of the brand emblem in circles on deep red, fading from dark to bright red"></section>
</main>
</body>
</html>
```